Vellora Labs - Mushroom Supplement Packaging

Our brand is called Vellora Labs. I've added a couple different logos that you can use. We are creating a line up of Mushroom Supplement products. I will add the entire line-up of products here. I've added examples of other products and packaging shape types I can purchase. Give me different options for packaging that is minimalist and clean for this brand that makes it look really well made and clean and make people want to buy.

Product 1 Lions Mane 1g
Product 2 Cordyceps 1g
Product 3 Chaga 1g
Product 4 Turkey Tail 1g
Product 5 Reishi 1g
Product 6 Maitake 1g
Product 7 Shiitake 1g

Product 8 (Mix) Lions Mane 143mg
Cordyceps 143mg
Chaga 143mg
Turkey Tail 143mg
Reishi 143mg
Maitake 143mg
Shiitake 143mg

```html
<!DOCTYPE html>
<html lang="en">
<head>
<meta charset="utf-8">
<title>Vellora Labs – Mushroom Extract Capsules Label Range</title>
<link rel="stylesheet" href="https://fonts.googleapis.com/css2?family=Bebas+Neue&family=Michroma&family=Open+Sans:wght@700&family=Saira+Condensed:wght@700&display=swap">
<style>
  :root{
    --paper:#ffffff;
    --label-body:#f4f4f5;
    --ink:#2b2b2b;
    --white:#ffffff;
    --blue:#3b93e6;
    --red:#d23f38;
    --sky:#7ab6d6;
    --green:#2f9e5a;
    --purple:#6e55a6;
    --yellow:#ddaa2c;
    --teal:#4fa9a0;
    --orange:#e07a3a;
  }
  *{box-sizing:border-box;margin:0;padding:0}
  html,body{width:1200px;height:960px;overflow:hidden;background:var(--paper)}
  .range{
    width:1200px;height:960px;
    display:grid;
    grid-template-columns:repeat(4,270px);
    grid-template-rows:repeat(2,370px);
    gap:70px 20px;
    justify-content:center;
    align-content:center;
  }
  .label{
    --accent:var(--blue);
    position:relative;
    background:var(--label-body);
    border-radius:6px;
    overflow:hidden;
    box-shadow:0 2px 10px rgba(0,0,0,.08);
  }
  .label--lions-mane{--accent:var(--blue)}
  .label--chaga{--accent:var(--red)}
  .label--turkey-tail{--accent:var(--sky)}
  .label--shiitake{--accent:var(--green)}
  .label--blend{--accent:var(--purple)}
  .label--cordyceps{--accent:var(--yellow)}
  .label--maitake{--accent:var(--teal)}
  .label--reishi{--accent:var(--orange)}

  .label__band{
    height:112px;
    background:var(--accent);
    display:flex;align-items:center;justify-content:space-between;
    padding:0 18px;
  }
  .brand{
    display:flex;align-items:center;gap:6px;
    font-family:"Bebas Neue",sans-serif;
    font-size:28px;line-height:.9;
    color:var(--white);
    letter-spacing:.5px;
  }
  .brand__dot{width:12px;height:12px;border-radius:50%;background:var(--white);flex:none}
  .band__claim{
    font-family:"Saira Condensed",sans-serif;
    font-weight:700;font-size:17px;line-height:1.05;
    color:var(--white);
    text-transform:uppercase;
  }
  .label__content{padding:18px 16px 0}
  .product-name{
    font-family:"Bebas Neue",sans-serif;
    font-size:60px;line-height:.9;
    color:var(--accent);
    letter-spacing:-.5px;
    position:relative;z-index:2;
  }
  .product-benefit{
    margin-top:6px;
    font-family:"Michroma",sans-serif;
    font-size:8.5px;line-height:1.35;
    color:var(--ink);
    text-transform:uppercase;
    max-width:150px;
    position:relative;z-index:2;
  }
  .artwork{
    position:absolute;right:14px;bottom:64px;
    width:82px;height:80px;
    border-radius:40px 40px 10px 10px;
    background:linear-gradient(180deg,var(--accent),color-mix(in srgb,var(--accent) 70%,white));
    opacity:.95;
  }
  .supplement-type{
    position:absolute;left:16px;bottom:22px;
    font-family:"Open Sans",sans-serif;font-weight:700;
    font-size:10.5px;color:var(--ink);
    text-transform:uppercase;
  }
  .count{
    position:absolute;right:0;bottom:0;
    width:112px;height:64px;
    background:var(--accent);
    border-radius:26px 0 0 0;
    color:var(--white);
    display:flex;flex-direction:column;align-items:center;justify-content:center;
  }
  .count__number{font-family:"Michroma",sans-serif;font-size:19px;line-height:1}
  .count__unit{font-family:"Open Sans",sans-serif;font-weight:700;font-size:6px;letter-spacing:.5px;margin-top:2px;text-transform:uppercase}
</style>
</head>
<body>
<main class="range">

  <article class="label label--lions-mane">
    <header class="label__band">
      <div class="brand"><span class="brand__dot"></span>Vellora<br>Labs</div>
      <p class="band__claim">Mushroom<br>Extract<br>Capsules</p>
    </header>
    <div class="label__content">
      <h2 class="product-name">Lion's Mane</h2>
      <p class="product-benefit">Focus, clarity &amp; mood</p>
    </div>
    <div class="artwork" role="img" aria-label="Mushroom cluster illustration"></div>
    <p class="supplement-type">Dietary Supplement</p>
    <div class="count"><span class="count__number">120</span><span class="count__unit">Capsules</span></div>
  </article>

  <article class="label label--chaga">
    <header class="label__band">
      <div class="brand"><span class="brand__dot"></span>Vellora<br>Labs</div>
      <p class="band__claim">Mushroom<br>Extract<br>Capsules</p>
    </header>
    <div class="label__content">
      <h2 class="product-name">Chaga</h2>
      <p class="product-benefit">Immune support, antioxidant support &amp; digestive health</p>
    </div>
    <div class="artwork" role="img" aria-label="Mushroom cluster illustration"></div>
    <p class="supplement-type">Dietary Supplement</p>
    <div class="count"><span class="count__number">120</span><span class="count__unit">Capsules</span></div>
  </article>

  <article class="label label--turkey-tail">
    <header class="label__band">
      <div class="brand"><span class="brand__dot"></span>Vellora<br>Labs</div>
      <p class="band__claim">Mushroom<br>Extract<br>Capsules</p>
    </header>
    <div class="label__content">
      <h2 class="product-name">Turkey Tail</h2>
      <p class="product-benefit">Immune support &amp; defence</p>
    </div>
    <div class="artwork" role="img" aria-label="Mushroom cluster illustration"></div>
    <p class="supplement-type">Dietary Supplement</p>
    <div class="count"><span class="count__number">120</span><span class="count__unit">Capsules</span></div>
  </article>

  <article class="label label--shiitake">
    <header class="label__band">
      <div class="brand"><span class="brand__dot"></span>Vellora<br>Labs</div>
      <p class="band__claim">Mushroom<br>Extract<br>Capsules</p>
    </header>
    <div class="label__content">
      <h2 class="product-name">Shiitake</h2>
      <p class="product-benefit">Immune support &amp; defence</p>
    </div>
    <div class="artwork" role="img" aria-label="Mushroom cluster illustration"></div>
    <p class="supplement-type">Dietary Supplement</p>
    <div class="count"><span class="count__number">120</span><span class="count__unit">Capsules</span></div>
  </article>

  <article class="label label--blend">
    <header class="label__band">
      <div class="brand"><span class="brand__dot"></span>Vellora<br>Labs</div>
      <p class="band__claim">Mushroom<br>Extract<br>Capsules</p>
    </header>
    <div class="label__content">
      <h2 class="product-name">Full Blend</h2>
      <p class="product-benefit">Lion's Mane, Cordyceps, Chaga, Turkey Tail, Reishi, Maitake &amp; Shiitake</p>
    </div>
    <div class="artwork" role="img" aria-label="Mushroom cluster illustration"></div>
    <p class="supplement-type">Dietary Supplement</p>
    <div class="count"><span class="count__number">120</span><span class="count__unit">Capsules</span></div>
  </article>

  <article class="label label--cordyceps">
    <header class="label__band">
      <div class="brand"><span class="brand__dot"></span>Vellora<br>Labs</div>
      <p class="band__claim">Mushroom<br>Extract<br>Capsules</p>
    </header>
    <div class="label__content">
      <h2 class="product-name">Cordyceps</h2>
      <p class="product-benefit">Energy support &amp; immune balancing properties</p>
    </div>
    <div class="artwork" role="img" aria-label="Mushroom cluster illustration"></div>
    <p class="supplement-type">Dietary Supplement</p>
    <div class="count"><span class="count__number">120</span><span class="count__unit">Capsules</span></div>
  </article>

  <article class="label label--maitake">
    <header class="label__band">
      <div class="brand"><span class="brand__dot"></span>Vellora<br>Labs</div>
      <p class="band__claim">Mushroom<br>Extract<br>Capsules</p>
    </header>
    <div class="label__content">
      <h2 class="product-name">Maitake</h2>
      <p class="product-benefit">Immune support &amp; metabolic balance</p>
    </div>
    <div class="artwork" role="img" aria-label="Mushroom cluster illustration"></div>
    <p class="supplement-type">Dietary Supplement</p>
    <div class="count"><span class="count__number">120</span><span class="count__unit">Capsules</span></div>
  </article>

  <article class="label label--reishi">
    <header class="label__band">
      <div class="brand"><span class="brand__dot"></span>Vellora<br>Labs</div>
      <p class="band__claim">Mushroom<br>Extract<br>Capsules</p>
    </header>
    <div class="label__content">
      <h2 class="product-name">Reishi</h2>
      <p class="product-benefit">Sleep support, relaxation &amp; stress relief</p>
    </div>
    <div class="artwork" role="img" aria-label="Mushroom cluster illustration"></div>
    <p class="supplement-type">Dietary Supplement</p>
    <div class="count"><span class="count__number">120</span><span class="count__unit">Capsules</span></div>
  </article>

</main>
</body>
</html>
```